Quiet Harbor Podcast Business Card Design

Needing a business card with the logo design provided for Quiet Harbor Podcast. I am looking for a modern style that fits the current logo.

Info:
Name: Teodor Vask
Title: Creator/Host
Email: teodor@quietharborcast.com
Phone: (555) 274-9163
www.quietharborcast.com
Twitter: @qharborcast
Instagram: @quietharborcastshow
Facebook: Quiet Harbor Podcast

Industry/Entity Type

Business

Font styles to use
Sans Serif

Colors
000000
ffffff

Requirements
Must have
• modern, clean design
Nice to have
• social media contact info

```html
<!DOCTYPE html>
<html lang="en">
<head>
<meta charset="utf-8">
<title>Quiet Harbor Podcast – Business Card</title>
<link rel="stylesheet" href="https://fonts.googleapis.com/css2?family=Montserrat:wght@400;500;700&display=swap">
<style>
  :root {
    --ink: #000000;
    --card-black: #0d0d0d;
    --paper: #ffffff;
    --stage: #3a3a3a;
    --muted: #3c3c3c;
    --map-tone-a: #262626;
    --map-tone-b: #151515;
  }
  * { box-sizing: border-box; margin: 0; padding: 0; }
  html, body {
    width: 1200px; height: 810px; overflow: hidden;
    background: var(--stage);
    font-family: "Montserrat", sans-serif;
  }
  .canvas { position: relative; width: 1200px; height: 810px; }
  .card {
    position: absolute; left: 290px; width: 620px; height: 354px;
    overflow: hidden;
  }
  .card--back { top: 31px; background: var(--card-black); color: var(--paper); }
  .card--front { top: 425px; background: var(--paper); color: var(--ink); }

  .world-map {
    position: absolute; left: 40px; top: 20px; width: 540px; height: 290px;
    border-radius: 40px;
    background: radial-gradient(ellipse at 50% 45%, var(--map-tone-a), var(--map-tone-b) 70%, transparent 100%);
  }
  .brand {
    position: absolute; text-align: center; display: flex; flex-direction: column;
    align-items: center; gap: 10px;
  }
  .brand__mark { width: 26px; height: 26px; }
  .brand__name {
    font-weight: 700; font-size: 30px; letter-spacing: 0.5px; line-height: 1.15;
    text-transform: uppercase;
  }
  .card--back .brand { left: 0; right: 0; top: 92px; }
  .card--back .brand__mark { background: var(--paper); }
  .back-url {
    position: absolute; left: 0; right: 0; top: 288px; text-align: center;
    font-size: 13px; letter-spacing: 1.5px;
  }

  .card--front .brand { left: 30px; width: 280px; top: 110px; }
  .card--front .brand__mark { background: var(--ink); }
  .card--front .brand__name { font-size: 26px; }
  .divider {
    position: absolute; left: 325px; top: 48px; width: 2px; height: 150px; background: var(--ink);
  }
  .contact { position: absolute; left: 345px; top: 40px; }
  .contact__name { font-size: 20px; font-weight: 500; letter-spacing: 1px; text-transform: uppercase; }
  .contact__title { font-size: 12px; letter-spacing: 1px; text-transform: uppercase; color: var(--muted); margin-bottom: 8px; }
  .contact__list { list-style: none; font-size: 12.5px; line-height: 18px; }
  .contact__list li { display: flex; align-items: center; gap: 9px; }
  .contact__list .gap { margin-top: 6px; }
  .icon { width: 11px; height: 11px; flex: none; }
  .icon--social { background: var(--ink); border-radius: 2px; width: 10px; height: 10px; }
  .wave { position: absolute; left: 0; bottom: 0; width: 620px; height: 150px; }
</style>
</head>
<body>
<main class="canvas">
  <section class="card card--back" aria-label="Card back">
    <div class="world-map" role="img" aria-label="Dotted world map in dark grey"></div>
    <div class="brand">
      <span class="brand__mark"></span>
      <span class="brand__name">Quiet Harbor Podcast</span>
    </div>
    <p class="back-url">www.quietharborcast.com</p>
  </section>

  <section class="card card--front" aria-label="Card front">
    <div class="brand">
      <span class="brand__mark"></span>
      <span class="brand__name">Quiet Harbor Podcast</span>
    </div>
    <div class="divider"></div>
    <div class="contact">
      <p class="contact__name">Teodor Vask</p>
      <p class="contact__title">Creator/Host</p>
      <ul class="contact__list">
        <li>
          <svg class="icon" viewBox="0 0 24 24"><path fill="#000" d="M6.6 10.8a15.1 15.1 0 0 0 6.6 6.6l2.2-2.2c.3-.3.7-.4 1-.2 1.1.4 2.3.6 3.6.6.6 0 1 .4 1 1V20c0 .6-.4 1-1 1A17 17 0 0 1 3 4c0-.6.4-1 1-1h3.5c.6 0 1 .4 1 1 0 1.3.2 2.5.6 3.6.1.3 0 .7-.2 1z"/></svg>
          (555) 274-9163
        </li>
        <li>
          <svg class="icon" viewBox="0 0 24 24"><path fill="#000" d="M2 5h20v14H2z"/><path fill="none" stroke="#fff" stroke-width="2" d="M2 5l10 8 10-8"/></svg>
          teodor@quietharborcast.com
        </li>
        <li>
          <svg class="icon" viewBox="0 0 24 24"><circle cx="12" cy="12" r="10" fill="#000"/></svg>
          www.quietharborcast.com
        </li>
        <li class="gap"><span class="icon icon--social"></span>Quiet Harbor Podcast</li>
        <li><span class="icon icon--social"></span>@qharborcast</li>
        <li><span class="icon icon--social"></span>@quietharborcastshow</li>
      </ul>
    </div>
    <svg class="wave" viewBox="0 0 620 150" preserveAspectRatio="none" aria-hidden="true">
      <path d="M0 150 L0 115 C140 55 330 150 470 95 C540 68 590 40 620 30 L620 150 Z" fill="#1a1a1a"/>
      <path d="M0 150 L0 128 C150 70 330 160 470 110 C545 82 590 55 620 45 L620 150 Z" fill="#ffffff"/>
      <path d="M0 150 L0 138 C150 85 330 168 470 122 C545 96 590 70 620 60 L620 150 Z" fill="#000000"/>
    </svg>
  </section>
</main>
</body>
</html>
```